General Power Point Presentation Pack

Hello Designers,

I am after a professional looking Microsoft PowerPoint deck that can be used for our corporate presentations. The pack should include a:

Title Page
Tittle and Content Page
Section Header Sheet
Two Content Page
Title Only Page
Blank Page
Content with Caption Page
Picture with Caption Page

I have included my brand guidelines and colours. I have also included some photos you may be able to use. Can you please ensure the pack has page numbering and that when you print it that it can be printed to full A4 Page.

Industry/Entity Type

Property Development & Construction

Requirements
Must have
• Prefer a white or very light coloured background

```html
<!DOCTYPE html>
<html lang="en">
<head>
<meta charset="utf-8">
<title>Keystone Presentation Pack</title>
<link href="https://fonts.googleapis.com/css2?family=Hind:wght@600;700&family=Open+Sans:ital,wght@0,400;0,600;1,400&display=swap" rel="stylesheet">
<style>
:root{
  --orange:#d9663a;
  --orange-line:#e49a72;
  --board:#c9c9c9;
  --white:#ffffff;
  --ink:#1f1f1f;
  --muted:#b3b3b3;
  --photo-interior:linear-gradient(160deg,#e9e4dc 0%,#cfc6b8 40%,#9aa08c 60%,#d8d1c4 100%);
  --photo-building:linear-gradient(180deg,#a9a6bd 0%,#c9a9a8 22%,#7b6357 45%,#5d4a40 65%,#4c5a39 82%,#6a6a62 100%);
  --photo-facade:linear-gradient(180deg,#c6d6e2 0%,#e8e5de 35%,#6b6255 60%,#b7a16a 75%,#4b5a3c 100%);
  --photo-kitchen:linear-gradient(135deg,#f1ede6 0%,#ddd6cb 45%,#c7b9a3 70%,#e6e1d8 100%);
  --photo-tower:linear-gradient(180deg,#8ea7c4 0%,#b4c3d4 30%,#4c4c50 55%,#7a4a38 80%,#4c5a3c 100%);
}
*{box-sizing:border-box;margin:0;padding:0}
html,body{width:676px;height:1200px;overflow:hidden;background:var(--board)}
.board{position:relative;width:676px;height:1200px;background:var(--board)}
.slide{position:absolute;width:309px;height:174px;background:var(--white);overflow:hidden;font-family:"Open Sans",Arial,sans-serif;color:var(--ink)}
.col-left{left:23px}.col-right{left:344px}
.row-1{top:38px}.row-2{top:226px}.row-3{top:412px}.row-4{top:599px}.row-5{top:785px}.row-6{top:972px}
.accent-bar{position:absolute;left:8px;top:0;width:5px;height:26px;background:var(--orange)}
.accent-tab{position:absolute;left:8px;top:0;width:34px;height:4px;background:var(--orange)}
.slide-title{position:absolute;left:20px;top:9px;font-family:"Hind",Arial,sans-serif;font-weight:700;font-size:9.5px;letter-spacing:.2px;color:var(--ink)}
.brand{position:absolute;right:9px;top:12px;font-family:"Hind",Arial,sans-serif;font-weight:600;font-size:6.5px;color:var(--orange);line-height:1}
.footer-line{position:absolute;left:8px;top:165px;width:287px;height:0;border-top:.6px solid var(--orange-line)}
.page-no{position:absolute;left:298px;top:161px;width:10px;height:8px;background:var(--orange);color:var(--white);font-size:3.5px;line-height:8px;text-align:center}
.photo{position:absolute}
.photo.interior{background:var(--photo-interior)}
.photo.building{background:var(--photo-building)}
.photo.facade{background:var(--photo-facade)}
.photo.kitchen{background:var(--photo-kitchen)}
.photo.tower{background:var(--photo-tower)}
.body-text{position:absolute;font-size:4.9px;line-height:6.2px;overflow:hidden}
.body-text p{margin-bottom:6px}
.sub-head{position:absolute;left:20px;top:91px;width:274px;color:var(--orange);font-weight:600;font-size:5.3px;padding-bottom:2px;border-bottom:.6px solid var(--orange-line)}
.caption{position:absolute;font-style:italic;font-size:4.7px;color:var(--muted)}
.caption-rule{position:absolute;height:0;border-top:.6px solid var(--orange-line)}
.orange-square{position:absolute;background:var(--orange)}
/* title slide */
.cover-panel{position:absolute;left:9px;top:0;width:142px;height:174px;background:rgba(217,102,58,.93)}
.cover-brand{position:absolute;left:9px;width:142px;top:56px;text-align:center;font-family:"Hind",Arial,sans-serif;font-weight:600;font-size:12px;color:var(--white)}
.cover-title{position:absolute;left:9px;width:142px;top:121px;text-align:center;font-family:"Hind",Arial,sans-serif;font-weight:700;font-size:15px;color:var(--white)}
.cover-rule{position:absolute;left:0;top:147px;width:309px;border-top:.6px solid rgba(255,255,255,.8)}
/* section header */
.section-panel{position:absolute;left:33px;top:0;width:68px;height:156px;background:rgba(217,102,58,.96)}
.section-title{position:absolute;left:33px;width:68px;top:73px;text-align:center;font-family:"Hind",Arial,sans-serif;font-weight:700;font-size:11.5px;line-height:13.5px;color:var(--white)}
/* closing */
.closing-panel{position:absolute;left:8px;top:0;width:104px;height:174px;background:var(--orange)}
.closing-title{position:absolute;left:30px;top:62px;font-family:"Hind",Arial,sans-serif;font-weight:700;font-size:19px;line-height:23px;color:var(--white)}
.closing-brand{position:absolute;left:160px;top:80px;width:100px;text-align:center;font-family:"Hind",Arial,sans-serif;font-weight:600;font-size:18px;color:var(--orange)}
.closing-line{left:112px;width:183px}
</style>
</head>
<body>
<div class="board">

  <!-- Title page -->
  <section class="slide col-left row-1">
    <div class="photo interior" style="left:0;top:9px;width:309px;height:138px" role="img" aria-label="Photo of a bright apartment living room with sofa, dining table and garden view"></div>
    <div class="cover-panel"></div>
    <div class="cover-brand">Keystone</div>
    <div class="cover-title">Title Goes Here</div>
    <div class="cover-rule"></div>
  </section>

  <!-- Title and content -->
  <section class="slide col-right row-1">
    <div class="accent-bar"></div>
    <h2 class="slide-title">TITLE GOES HERE</h2>
    <div class="brand">Keystone</div>
    <div class="body-text" style="left:20px;top:30px;width:275px;height:59px">
      <p>Lorem ipsum dolor sit amet, consectetuer adipiscing elit. Maecenas porttitor congue massa. Fusce posuere, magna sed pulvinar ultricies, purus lectus malesuada libero, sit amet commodo magna eros quis urna.</p>
      <p>Nunc viverra imperdiet enim. Fusce est. Vivamus a tellus.</p>
      <p>Pellentesque habitant morbi tristique senectus et netus et malesuada fames ac turpis egestas. Proin pharetra nonummy pede. Mauris et orci.<br>Lorem ipsum dolor sit amet, consectetuer adipiscing elit. Maecenas porttitor congue massa. Fusce posuere, magna sed pulvinar ultricies, purus lectus malesuada libero, sit amet commodo magna eros quis urna.</p>
    </div>
    <div class="sub-head">Lorem ipsum dolor sit amet</div>
    <div class="body-text" style="left:21px;top:105px;width:274px;height:50px">
      <p>consectetuer adipiscing elit. Maecenas porttitor congue massa. Fusce posuere, magna sed pulvinar ultricies, purus lectus malesuada libero, sit amet commodo magna eros quis urna.</p>
      <p>Nunc viverra imperdiet enim. Fusce est. Vivamus a tellus.</p>
      <p>Pellentesque habitant morbi tristique senectus et netus et malesuada fames ac turpis egestas. Proin pharetra nonummy pede. Mauris et orci.<br>Lorem ipsum dolor sit amet, consectetuer adipiscing elit. Maecenas porttitor congue massa. Fusce posuere, magna sed</p>
    </div>
    <div class="footer-line"></div><div class="page-no">1</div>
  </section>

  <!-- Two content -->
  <section class="slide col-left row-2">
    <div class="accent-bar"></div>
    <h2 class="slide-title">TITLE GOES HERE</h2>
    <div class="brand">Keystone</div>
    <div class="body-text" style="left:20px;top:29px;width:98px;height:115px">
      <p>Lorem ipsum dolor sit amet, consectetuer adipiscing elit. Maecenas porttitor congue massa. Fusce posuere, magna sed pulvinar ultricies, purus lectus malesuada libero, sit amet commodo magna eros quis urna.</p>
      <p>Nunc viverra imperdiet enim. Fusce est. Vivamus a tellus.</p>
      <p>Pellentesque habitant morbi tristique senectus et netus et malesuada fames ac turpis egestas. Proin pharetra nonummy pede. Mauris et orci.<br>Lorem ipsum dolor sit amet, consectetuer adipiscing elit. Maecenas porttitor congue massa. Fusce posuere, magna sed pulvinar ultricies, purus lectus malesuada libero, sit amet commodo magna eros quis urna.</p>
    </div>
    <div class="body-text" style="left:137px;top:29px;width:154px;height:115px">
      <p>Lorem ipsum dolor sit amet, consectetuer adipiscing elit. Maecenas porttitor congue massa. Fusce posuere, magna sed pulvinar ultricies, purus lectus malesuada libero, sit amet commodo magna eros quis urna.</p>
      <p>Nunc viverra imperdiet enim. Fusce est. Vivamus a tellus.</p>
      <p>Pellentesque habitant morbi tristique senectus et netus et malesuada fames ac turpis egestas. Proin pharetra nonummy pede. Mauris et orci.<br>Lorem ipsum dolor sit amet, consectetuer adipiscing elit. Maecenas porttitor congue massa. Fusce posuere, magna sed pulvinar ultricies, purus lectus malesuada libero, sit amet commodo magna eros quis urna. Pulvina r ultricies, purus lectus malesuada libero, sit amet commodo magna eros quis urna.</p>
    </div>
    <div class="footer-line"></div><div class="page-no">2</div>
  </section>

  <!-- Content with picture -->
  <section class="slide col-right row-2">
    <div class="accent-bar"></div>
    <h2 class="slide-title">TITLE GOES HERE</h2>
    <div class="brand">Keystone</div>
    <div class="body-text" style="left:20px;top:29px;width:98px;height:115px">
      <p>Lorem ipsum dolor sit amet, consectetuer adipiscing elit. Maecenas porttitor congue massa. Fusce posuere, magna sed pulvinar ultricies, purus lectus malesuada libero, sit amet commodo magna eros quis urna.</p>
      <p>Nunc viverra imperdiet enim. Fusce est. Vivamus a tellus.</p>
      <p>Pellentesque habitant morbi tristique senectus et netus et malesuada fames ac turpis egestas. Proin pharetra nonummy pede. Mauris et orci.<br>Lorem ipsum dolor sit amet, consectetuer adipiscing elit. Maecenas porttitor congue massa. Fusce posuere, magna sed pulvinar ultricies, purus lectus malesuada libero, sit amet commodo magna eros quis urna.</p>
    </div>
    <div class="orange-square" style="left:131px;top:24px;width:19px;height:19px"></div>
    <div class="photo building" style="left:135px;top:28px;width:174px;height:115px" role="img" aria-label="Dusk rendering of a brick apartment complex with palms and landscaped entry"></div>
    <div class="footer-line"></div><div class="page-no">3</div>
  </section>

  <!-- Section header -->
  <section class="slide col-left row-3">
    <div class="brand">Keystone</div>
    <div class="photo facade" style="left:0;top:35px;width:309px;height:98px" role="img" aria-label="Rendering of a modern apartment facade with balconies and greenery"></div>
    <div class="section-panel"></div>
    <div class="section-title">SECTION<br>HEADER</div>
    <div class="footer-line"></div><div class="page-no">4</div>
  </section>

  <!-- Title only with pictures -->
  <section class="slide col-right row-3">
    <div class="accent-bar"></div>
    <h2 class="slide-title">TITLE GOES HERE</h2>
    <div class="brand">Keystone</div>
    <div class="photo kitchen" style="left:0;top:25px;width:182px;height:134px" role="img" aria-label="Interior of a modern kitchen with marble island and dining area"></div>
    <div class="photo tower" style="left:185px;top:25px;width:124px;height:134px" role="img" aria-label="Rendering of a multi-storey apartment building on a street corner"></div>
    <div class="footer-line"></div><div class="page-no">5</div>
  </section>

  <!-- Blank -->
  <section class="slide col-left row-4">
    <div class="accent-tab"></div>
    <div class="brand">Keystone</div>
    <div class="footer-line"></div><div class="page-no">6</div>
  </section>

  <!-- Content with caption -->
  <section class="slide col-right row-4">
    <div class="accent-bar"></div>
    <h2 class="slide-title">TITLE GOES HERE</h2>
    <div class="brand">Keystone</div>
    <div class="body-text" style="left:20px;top:29px;width:123px;height:44px">
      <p>Lorem ipsum dolor sit amet, consectetuer adipiscing elit. Maecenas porttitor congue massa. Fusce posuere, magna sed pulvinar ultricies, purus lectus malesuada libero, sit amet commodo magna eros quis urna.</p>
      <p>Nunc viverra imperdiet enim. Fusce est. Vivamus a tellus.</p>
    </div>
    <div class="caption-rule" style="left:20px;top:75px;width:123px"></div>
    <div class="caption" style="left:20px;top:77px">Lorem ipsum dolor sit</div>
    <div class="body-text" style="left:154px;top:29px;width:141px;height:44px">
      <p>Lorem ipsum dolor sit amet, consectetuer adipiscing elit. Maecenas porttitor congue massa. Fusce posuere, magna sed pulvinar ultricies, purus lectus malesuada libero, sit amet commodo magna eros quis urna.</p>
      <p>Nunc viverra imperdiet enim. Fusce est. Vivamus a tellus.</p>
    </div>
    <div class="caption-rule" style="left:154px;top:75px;width:141px"></div>
    <div class="caption" style="left:154px;top:77px">Lorem ipsum dolor sit</div>
    <div class="body-text" style="left:20px;top:98px;width:123px;height:44px">
      <p>Lorem ipsum dolor sit amet, consectetuer adipiscing elit. Maecenas porttitor congue massa. Fusce posuere, magna sed pulvinar ultricies, purus lectus malesuada libero, sit amet commodo magna eros quis urna.</p>
      <p>Nunc viverra imperdiet enim. Fusce est. Vivamus a tellus.</p>
    </div>
    <div class="caption-rule" style="left:20px;top:143px;width:123px"></div>
    <div class="caption" style="left:20px;top:145px">Lorem ipsum dolor sit</div>
    <div class="body-text" style="left:154px;top:98px;width:141px;height:44px">
      <p>Lorem ipsum dolor sit amet, consectetuer adipiscing elit. Maecenas porttitor congue massa. Fusce posuere, magna sed pulvinar ultricies, purus lectus malesuada libero, sit amet commodo magna eros quis urna.</p>
      <p>Nunc viverra imperdiet enim. Fusce est. Vivamus a tellus.</p>
    </div>
    <div class="caption-rule" style="left:154px;top:143px;width:141px"></div>
    <div class="caption" style="left:154px;top:145px">Lorem ipsum dolor sit</div>
    <div class="footer-line"></div><div class="page-no">7</div>
  </section>

  <!-- Four pictures with captions -->
  <section class="slide col-left row-5">
    <div class="accent-bar"></div>
    <h2 class="slide-title">TITLE GOES HERE</h2>
    <div class="brand">Keystone</div>
    <div class="photo building" style="left:20px;top:31px;width:122px;height:51px" role="img" aria-label="Dusk rendering of the apartment complex entry"></div>
    <div class="caption-rule" style="left:20px;top:82px;width:122px"></div>
    <div class="caption" style="left:20px;top:84px">Lorem ipsum dolor sit</div>
    <div class="photo building" style="left:164px;top:31px;width:122px;height:51px" role="img" aria-label="Dusk rendering of the apartment complex entry"></div>
    <div class="caption-rule" style="left:164px;top:82px;width:122px"></div>
    <div class="caption" style="left:164px;top:84px">Lorem ipsum dolor sit</div>
    <div class="photo building" style="left:20px;top:98px;width:122px;height:51px" role="img" aria-label="Dusk rendering of the apartment complex entry"></div>
    <div class="caption-rule" style="left:20px;top:149px;width:122px"></div>
    <div class="caption" style="left:20px;top:151px">Lorem ipsum dolor sit</div>
    <div class="photo building" style="left:164px;top:98px;width:122px;height:51px" role="img" aria-label="Dusk rendering of the apartment complex entry"></div>
    <div class="caption-rule" style="left:164px;top:149px;width:122px"></div>
    <div class="caption" style="left:164px;top:151px">Lorem ipsum dolor sit</div>
    <div class="footer-line"></div><div class="page-no">8</div>
  </section>

  <!-- Picture with caption -->
  <section class="slide col-right row-5">
    <div class="accent-bar"></div>
    <h2 class="slide-title">TITLE GOES HERE</h2>
    <div class="brand">Keystone</div>
    <div class="photo building" style="left:20px;top:31px;width:208px;height:85px" role="img" aria-label="Dusk rendering of the apartment complex with palms"></div>
    <div class="caption" style="left:23px;top:121px">Lorem ipsum dolor sit</div>
    <div class="caption" style="left:234px;top:58px">Lorem ipsum dolor sit</div>
    <div class="photo building" style="left:192px;top:70px;width:103px;height:85px" role="img" aria-label="Close view of the apartment complex entry garden"></div>
    <div class="footer-line"></div><div class="page-no">9</div>
  </section>

  <section class="slide col-left row-6">
    <div class="accent-bar"></div>
    <h2 class="slide-title">TITLE GOES HERE</h2>
    <div class="brand">Keystone</div>
    <div class="photo building" style="left:20px;top:31px;width:208px;height:85px" role="img" aria-label="Dusk rendering of the apartment complex with palms"></div>
    <div class="caption" style="left:23px;top:121px">Lorem ipsum dolor sit</div>
    <div class="caption" style="left:234px;top:58px">Lorem ipsum dolor sit</div>
    <div class="photo building" style="left:192px;top:70px;width:103px;height:85px" role="img" aria-label="Close view of the apartment complex entry garden"></div>
    <div class="footer-line"></div><div class="page-no">10</div>
  </section>

  <!-- Closing -->
  <section class="slide col-right row-6">
    <div class="closing-panel"></div>
    <div class="closing-title">THANK<br>YOU</div>
    <div class="closing-brand">Keystone</div>
    <div class="footer-line closing-line"></div><div class="page-no">10</div>
  </section>

</div>
</body>
</html>
```